homepage design , industry automation control image

we need a design , based on our Logo image.

we focus on selling of temprature sensor ,and parts.

but need concept or image on industry automation control

we need enviroment friendly concept.

Industry/Entity Type

Industry

Number of Pages Required

5+ page

Requirements
Must have
• we need a Cartoon Image of a Temperature sensor,
• attaching a Excel file with the sensor looking.
Nice to have
• Nature image, future concept

```html
<!DOCTYPE html>
<html lang="en">
<head>
<meta charset="utf-8">
<title>Lindqvist Messtechnik – Home</title>
<link rel="stylesheet" href="https://fonts.googleapis.com/css2?family=Questrial&family=Open+Sans:wght@400;600&display=swap">
<style>
  :root{
    --green:#2a9a2a;
    --green-dark:#138a13;
    --green-bright:#5cc41a;
    --heading-green:#1f8a1f;
    --text:#555;
    --text-light:#888;
    --line:#e3e3e3;
    --panel:#f7f7f7;
    --white:#fff;
    --dark:#333;
    --social-a:#3b5aa0;
    --social-b:#2aa3e6;
  }
  *{box-sizing:border-box;margin:0;padding:0}
  html,body{width:710px;height:1200px;overflow:hidden;background:var(--white)}
  body{font-family:"Open Sans",Arial,sans-serif;color:var(--text);position:relative}
  .heading{font-family:"Questrial","Century Gothic",sans-serif;font-weight:400}

  /* header */
  .site-header{position:absolute;top:0;left:0;width:710px;height:58px;background:var(--white)}
  .brand{position:absolute;left:78px;top:15px;display:flex;align-items:center;gap:5px}
  .brand-mark{width:28px;height:28px;background:var(--green-bright)}
  .brand-name{font-family:"Questrial",sans-serif;font-size:16px;color:var(--green-dark);font-weight:400}
  .main-nav{position:absolute;right:79px;top:26px;display:flex;gap:18px;font-size:7px;line-height:9px}
  .main-nav a{color:var(--dark);text-decoration:none}
  .main-nav a.active{color:var(--green)}

  /* hero */
  .hero{position:absolute;top:58px;left:0;width:710px;height:305px;
    background:linear-gradient(100deg,#3a3a3a 0%,#b8b2a8 30%,#d9d2c4 55%,#6b5a48 70%,#e4ddd0 100%)}
  .hero-arrow{position:absolute;top:143px;width:15px;height:20px;display:flex;align-items:center;justify-content:center}
  .hero-arrow.prev{left:0}
  .hero-arrow.next{right:0;background:#777}

  /* welcome */
  .welcome{position:absolute;top:363px;left:0;width:710px;height:189px;
    background:linear-gradient(180deg,#2e9b2e 0%,#259225 60%,#1e851e 100%)}
  .welcome-photo{position:absolute;left:78px;top:45px;width:129px;height:99px;
    background:linear-gradient(180deg,#9db7d6 0%,#b7c7d4 40%,#4f6b3a 70%,#2f4a22 100%)}
  .welcome-body{position:absolute;left:220px;top:42px;width:412px;color:var(--white)}
  .welcome-body h1{font-size:15px;line-height:18px;margin-bottom:6px}
  .welcome-body p{font-size:6.3px;line-height:12.5px}
  .btn-light{display:inline-block;margin-top:8px;background:var(--white);color:var(--dark);font-size:6px;line-height:8px;padding:6px 10px;text-decoration:none}

  /* services */
  .services{position:absolute;top:552px;left:0;width:710px;height:248px;background:var(--white)}
  .service{position:absolute;top:47px;width:164px;text-align:center}
  .service-icon{width:48px;height:48px;margin:0 auto;background:linear-gradient(180deg,#4cc01c,#1a9a12);display:flex;align-items:center;justify-content:center}
  .service h2{font-size:15px;line-height:18px;color:var(--heading-green);margin-top:10px}
  .service p{font-size:5.6px;line-height:9.5px;color:var(--text-light);margin-top:6px}
  .btn-outline{display:inline-block;margin-top:9px;border:1px solid #ccc;color:var(--text-light);font-size:6px;line-height:8px;padding:6px 11px;text-decoration:none}

  /* news */
  .news{position:absolute;top:800px;left:0;width:710px;height:239px;background:var(--panel)}
  .news h2{position:absolute;left:78px;top:40px;font-size:14.5px;line-height:18px;color:var(--heading-green)}
  .view-all{position:absolute;right:79px;top:47px;font-size:5.5px;line-height:7px;color:var(--dark);display:flex;align-items:center;gap:3px}
  .news-card{position:absolute;top:68px;width:129px;height:129px;background:var(--white);box-shadow:0 1px 3px rgba(0,0,0,.12);padding:18px 14px}
  .news-card time{display:block;font-size:7.2px;line-height:9px;color:var(--dark)}
  .news-card p{font-size:5.6px;line-height:10.4px;color:var(--text-light);margin-top:8px}
  .more{display:flex;align-items:center;gap:3px;font-size:5.5px;line-height:7px;color:var(--dark);margin-top:12px}

  /* footer */
  .site-footer{position:absolute;top:1039px;left:0;width:710px;height:109px;border-top:1px solid var(--line);background:var(--white)}
  .footer-title{font-size:9.5px;line-height:12px;color:var(--dark)}
  .contact{position:absolute;left:78px;top:27px}
  .contact ul{list-style:none}
  .contact li{display:flex;align-items:center;gap:6px;font-size:5.6px;line-height:8px;color:var(--text-light);margin-top:6px}
  .map{position:absolute;left:242px;top:42px;width:111px;height:47px;border:2px solid var(--white);box-shadow:0 0 2px rgba(0,0,0,.2);
    background:linear-gradient(120deg,#e7e4dc 0%,#d8e5c9 50%,#b7cfe8 80%,#e7e4dc 100%)}
  .links{position:absolute;left:406px;top:27px}
  .links ul{list-style:none;display:grid;grid-template-columns:62px 80px;row-gap:5px;margin-top:6px}
  .links li{font-size:5.6px;line-height:9px}
  .links a{color:var(--text-light);text-decoration:none}
  .social{position:absolute;left:575px;top:27px}
  .social-icons{display:flex;gap:4px;margin-top:6px}
  .social-icons span{width:15px;height:15px;border-radius:50%}
  .copyright{position:absolute;top:1148px;left:0;width:710px;height:52px;border-top:1px solid var(--line);text-align:center;font-size:6px;line-height:8px;color:var(--dark);padding-top:22px}
</style>
</head>
<body>

<header class="site-header">
  <div class="brand">
    <span class="brand-mark"></span>
    <span class="brand-name">Lindqvist Messtechnik</span>
  </div>
  <nav class="main-nav">
    <a href="#" class="active">Home</a>
    <a href="#">About Us</a>
    <a href="#">Products</a>
    <a href="#">Technology</a>
    <a href="#">Media</a>
    <a href="#">Contact Us</a>
  </nav>
</header>

<section class="hero" role="img" aria-label="Hand holding a thermal imaging camera in front of industrial circuit breakers">
  <span class="hero-arrow prev"><svg width="6" height="12" viewBox="0 0 6 12"><path d="M5 1 1 6l4 5" fill="none" stroke="#fff" stroke-width="1"/></svg></span>
  <span class="hero-arrow next"><svg width="6" height="12" viewBox="0 0 6 12"><path d="M1 1l4 5-4 5" fill="none" stroke="#fff" stroke-width="1"/></svg></span>
</section>

<section class="welcome" aria-label="Welcome">
  <div class="welcome-photo" role="img" aria-label="City tower rising above a green landscape"></div>
  <div class="welcome-body">
    <h1 class="heading">Welcome to Lindqvist Messtechnik</h1>
    <p>Pellentesque porttitor suscipit sapien, ac imperdiet nibh fringilla et. Quisque eu urna metus. Integer sed nisi in dui sagittis blandit et at elit. Suspendisse vulputate dictum placerat. Pellentesque ut sodales libero, vel mattis tortor. Suspendisse sapien est, tempus et tellus eget, dapibus lacinia enim. Nunc porttitor nisi eget magna faucibus, eget vestibulum mi scelerisque. Cras aliquet augue nec condimentum egestas. Vestibulum a tortor dictum, sodales purus nec, consequat felis.</p>
    <a href="#" class="btn-light">Read more</a>
  </div>
</section>

<section class="services">
  <article class="service" style="left:76px">
    <div class="service-icon">
      <svg width="24" height="30" viewBox="0 0 24 30" fill="none" stroke="#fff" stroke-width="1.5"><path d="M9 3a3 3 0 0 1 6 0v15a6 6 0 1 1-6 0z"/><path d="M12 10v11"/><path d="M17 6h3M17 10h3M17 14h3"/></svg>
    </div>
    <h2 class="heading">Temperature Sensor<br>and Parts</h2>
    <p>Suspendisse sapien est, tempus et tellus eget, dapibus lacinia enim. Nunc porttitor nisi eget magna faucibus, eget vestibulum mi scelerisque.</p>
    <a href="#" class="btn-outline">View more</a>
  </article>
  <article class="service" style="left:273px">
    <div class="service-icon">
      <svg width="30" height="28" viewBox="0 0 30 28" fill="none" stroke="#fff" stroke-width="1.5"><path d="M3 25h24M6 25v-3h18v3"/><circle cx="10" cy="8" r="3"/><path d="M10 11v11M12 7l9-3 3 4M24 8v4l-2 2M24 12l2 2"/></svg>
    </div>
    <h2 class="heading">Industry Automation<br>Control</h2>
    <p>Suspendisse sapien est, tempus et tellus eget, dapibus lacinia enim. Nunc porttitor nisi eget magna faucibus, eget vestibulum mi scelerisque.</p>
    <a href="#" class="btn-outline">View more</a>
  </article>
  <article class="service" style="left:469px">
    <div class="service-icon">
      <svg width="28" height="30" viewBox="0 0 28 30" fill="none" stroke="#fff" stroke-width="1.5"><circle cx="14" cy="12" r="10"/><circle cx="14" cy="12" r="6.5"/><path d="M14 12l3-4M14 22v4M8 27h12"/></svg>
    </div>
    <h2 class="heading">Industry Pressure<br>Control</h2>
    <p>Suspendisse sapien est, tempus et tellus eget, dapibus lacinia enim. Nunc porttitor nisi eget magna faucibus, eget vestibulum mi scelerisque.</p>
    <a href="#" class="btn-outline">View more</a>
  </article>
</section>

<section class="news">
  <h2 class="heading">Latest News</h2>
  <a class="view-all">VIEW ALL <svg width="6" height="6" viewBox="0 0 6 6"><circle cx="3" cy="3" r="3" fill="#333"/><path d="M2.3 1.6 3.7 3 2.3 4.4" stroke="#fff" stroke-width=".8" fill="none"/></svg></a>
  <article class="news-card" style="left:78px">
    <time>23 March, 2017</time>
    <p>Curabitur quis leo mattis, malesuada quam et, semper felis. Proin facilisis ultrices felis, eu laoreet sem ullamcorper ultrices. Vestibulum ullamcorper, dolor</p>
    <span class="more">MORE <svg width="6" height="6" viewBox="0 0 6 6"><circle cx="3" cy="3" r="3" fill="#333"/><path d="M2.3 1.6 3.7 3 2.3 4.4" stroke="#fff" stroke-width=".8" fill="none"/></svg></span>
  </article>
  <article class="news-card" style="left:220px">
    <time>23 March, 2017</time>
    <p>Curabitur quis leo mattis, malesuada quam et, semper felis. Proin facilisis ultrices felis, eu laoreet sem ullamcorper ultrices. Vestibulum ullamcorper, dolor</p>
    <span class="more">MORE <svg width="6" height="6" viewBox="0 0 6 6"><circle cx="3" cy="3" r="3" fill="#333"/><path d="M2.3 1.6 3.7 3 2.3 4.4" stroke="#fff" stroke-width=".8" fill="none"/></svg></span>
  </article>
  <article class="news-card" style="left:362px">
    <time>23 March, 2017</time>
    <p>Curabitur quis leo mattis, malesuada quam et, semper felis. Proin facilisis ultrices felis, eu laoreet sem ullamcorper ultrices. Vestibulum ullamcorper, dolor</p>
    <span class="more">MORE <svg width="6" height="6" viewBox="0 0 6 6"><circle cx="3" cy="3" r="3" fill="#333"/><path d="M2.3 1.6 3.7 3 2.3 4.4" stroke="#fff" stroke-width=".8" fill="none"/></svg></span>
  </article>
  <article class="news-card" style="left:503px">
    <time>23 March, 2017</time>
    <p>Curabitur quis leo mattis, malesuada quam et, semper felis. Proin facilisis ultrices felis, eu laoreet sem ullamcorper ultrices. Vestibulum ullamcorper, dolor</p>
    <span class="more">MORE <svg width="6" height="6" viewBox="0 0 6 6"><circle cx="3" cy="3" r="3" fill="#333"/><path d="M2.3 1.6 3.7 3 2.3 4.4" stroke="#fff" stroke-width=".8" fill="none"/></svg></span>
  </article>
</section>

<footer class="site-footer">
  <div class="contact">
    <h3 class="footer-title heading">Contact Us</h3>
    <ul>
      <li><svg width="5" height="6" viewBox="0 0 5 6"><path d="M2.5 6S0 3.4 0 2.3a2.5 2.5 0 0 1 5 0C5 3.4 2.5 6 2.5 6z" fill="#999"/></svg>24 Building name, Street name, Fairhaven, AZ</li>
      <li><svg width="5" height="6" viewBox="0 0 5 6"><rect x="1" y="0" width="3" height="6" rx=".5" fill="#999"/></svg>248.555.0148</li>
      <li><svg width="5" height="6" viewBox="0 0 5 6"><rect x="0" y="1.5" width="5" height="3.5" fill="#999"/></svg>Email : info@lindqvistmess.com</li>
    </ul>
  </div>
  <div class="map" role="img" aria-label="Street map showing the office location"></div>
  <nav class="links">
    <h3 class="footer-title heading">Links</h3>
    <ul>
      <li><a href="#">Home</a></li><li><a href="#">Media</a></li>
      <li><a href="#">About Us</a></li><li><a href="#">Contact Us</a></li>
      <li><a href="#">Products</a></li><li><a href="#">Terms and Conditions</a></li>
      <li><a href="#">Technology</a></li>
    </ul>
  </nav>
  <div class="social">
    <h3 class="footer-title heading">Follow us on</h3>
    <div class="social-icons">
      <span style="background:var(--social-a)"></span>
      <span style="background:var(--social-b)"></span>
    </div>
  </div>
</footer>

<div class="copyright">Copyright © 2017 Company name. All rights reserved.</div>

</body>
</html>
```